We need a poster designed for use on facebook, as well as to print out for advertising in local noticeboards and shop windows.
The poster will advertise the Fernhollow Turf Society 30th Anniversary Ball.
the ball will be held on the 28th April 2018 at the Fernhollow Community Hall.
Time will be 630pm till late. Ticket Price is $120 which includes 3 course dinner, drinks on arrival and entertainment during the evening.
Additional details will need to be added to the poster at a later date.
The fernhollow Turf Society is a horse racing club run by the community. The club has been incorporateds for 30 years. This Ball will be a celebration of that anniversary.

Target Market(s)

Middlemount Community

Industry/Entity Type

Club

Font styles to use
Serif
Decorative

Colors
1b1b1b
fbfbfb
6b449b
886aae
a64599
ffc214

Requirements
Must have
• Include
• where when time and cost
• ticket inclusions
• entertainement by Colin Hartwell
Nice to have
• Attached are some images for inspiration.
• It would be nice to have the race club logo included somewhere however not prominant.
Should not have
• Abstract geometriic lines
• images of people
• primary colours

```html
<!DOCTYPE html>
<html lang="en">
<head>
<meta charset="utf-8">
<title>Fernhollow Turf Society 30th Anniversary Ball</title>
<link rel="stylesheet" href="https://fonts.googleapis.com/css2?family=Playfair+Display:wght@400;600;700;800;900&family=Lora:wght@400;600;700&display=swap">
<style>
  :root {
    --page-bg: #e6e6e6;
    --poster-dark: #1b1b1b;
    --poster-mid: #2c2533;
    --purple: #6b449b;
    --lavender: #886aae;
    --magenta: #a64599;
    --gold: #ffc214;
    --text-white: #fbfbfb;
    --text-muted: #d4cfdc;
    --photo-deep: #1f1a1f;
    --photo-warm: #5a2d20;
    --photo-light: #8a4a35;
    --portrait-tone: #b98a6a;
  }
  * { margin: 0; padding: 0; box-sizing: border-box; }
  html, body {
    width: 1200px; height: 2556px; overflow: hidden;
    background: var(--page-bg);
  }
  .poster {
    position: absolute; left: 50px; top: 518px;
    width: 1100px; height: 1520px; overflow: hidden;
    background: radial-gradient(ellipse at 58% 38%, var(--poster-mid) 0%, var(--poster-dark) 68%);
    color: var(--text-white);
    font-family: "Lora", Georgia, serif;
  }
  .club-mark {
    position: absolute; left: 45px; top: 55px;
    width: 300px; display: flex; align-items: center; gap: 14px;
  }
  .club-mark-dot {
    width: 46px; height: 46px; border-radius: 50%;
    background: var(--gold); flex-shrink: 0;
  }
  .club-mark-name {
    font-family: "Playfair Display", Georgia, serif;
    font-weight: 700; font-size: 27px; line-height: 1.15; color: var(--text-white);
  }
  .club-banner {
    position: absolute; left: 390px; top: 118px; width: 640px; height: 64px;
    background: var(--purple);
    font-family: "Playfair Display", Georgia, serif;
    font-weight: 600; font-size: 38px; line-height: 64px; text-align: center;
  }
  .headline {
    position: absolute; right: 70px; top: 192px; text-align: right;
    font-family: "Playfair Display", Georgia, serif;
    font-weight: 800; line-height: 1; white-space: nowrap;
  }
  .headline-main { font-size: 88px; }
  .headline-main sup { font-size: 44px; color: var(--gold); vertical-align: 36px; }
  .headline-sub { font-size: 50px; color: var(--gold); margin-top: 4px; letter-spacing: 2px; }
  .dancers-photo {
    position: absolute; left: 440px; top: 330px; width: 640px; height: 1100px;
    background: radial-gradient(ellipse 50% 50% at 50% 48%, var(--photo-light) 0%, var(--photo-warm) 40%, var(--photo-deep) 75%, rgba(27,27,27,0) 100%);
  }
  .event-badge {
    position: absolute; left: 20px; top: 470px; width: 430px; height: 430px;
    border-radius: 50%; background: var(--purple);
    border: 6px solid var(--lavender);
    display: flex; flex-direction: column; justify-content: center; align-items: center;
    text-align: center; line-height: 1.15;
  }
  .event-date { font-family: "Playfair Display", Georgia, serif; font-weight: 700; font-size: 42px; color: var(--gold); }
  .event-year { font-family: "Playfair Display", Georgia, serif; font-weight: 800; font-size: 64px; }
  .event-at { font-size: 28px; }
  .event-venue { font-family: "Playfair Display", Georgia, serif; font-weight: 700; font-size: 38px; }
  .event-time { font-size: 28px; margin-top: 10px; }
  .event-time strong { font-weight: 700; color: var(--gold); }
  .ticket {
    position: absolute; left: 75px; top: 960px; width: 430px;
  }
  .ticket-label { font-family: "Playfair Display", Georgia, serif; font-weight: 700; font-size: 42px; }
  .ticket-price { font-family: "Playfair Display", Georgia, serif; font-weight: 900; font-size: 100px; line-height: 1.05; color: var(--gold); }
  .ticket-includes { font-size: 25px; line-height: 1.35; color: var(--text-muted); margin-top: 6px; }
  .performer-photo {
    position: absolute; left: 75px; top: 1260px; width: 170px; height: 150px;
    background: linear-gradient(160deg, var(--portrait-tone), var(--photo-warm));
    border: 4px solid var(--lavender);
  }
  .performer {
    position: absolute; left: 280px; top: 1300px;
  }
  .performer-label { font-size: 23px; color: var(--lavender); }
  .performer-name { font-family: "Playfair Display", Georgia, serif; font-weight: 600; font-size: 46px; line-height: 1.1; }
  .site {
    position: absolute; right: 60px; top: 1440px;
    display: flex; align-items: center; gap: 16px;
    font-size: 26px;
  }
  .site-rule { width: 260px; height: 2px; background: var(--lavender); }
  .site-url .tld { color: var(--gold); }
</style>
</head>
<body>
  <main class="poster">
    <div class="club-mark">
      <span class="club-mark-dot"></span>
      <span class="club-mark-name">Fernhollow Turf Society</span>
    </div>

    <div class="club-banner">Fernhollow Turf Society</div>

    <h1 class="headline">
      <div class="headline-main">30<sup>th</sup>ANNIVERSARY</div>
      <div class="headline-sub">BALL</div>
    </h1>

    <div class="dancers-photo" role="img" aria-label="Photograph of a ballroom dancing couple in formal wear"></div>

    <section class="event-badge">
      <div class="event-date">28th April</div>
      <div class="event-year">2018</div>
      <div class="event-at">at the</div>
      <div class="event-venue">Fernhollow<br>Community Hall.</div>
      <div class="event-time">Time will be<br><strong>6.30pm</strong> till late</div>
    </section>

    <section class="ticket">
      <div class="ticket-label">Ticket Price Is</div>
      <div class="ticket-price">$120</div>
      <p class="ticket-includes">Which Includes 3 Course Dinner, Drinks On Arrival And Entertainment During the Evening.</p>
    </section>

    <div class="performer-photo" role="img" aria-label="Portrait photo of the performer"></div>
    <div class="performer">
      <div class="performer-label">Performance by</div>
      <div class="performer-name">Colin Hartwell</div>
    </div>

    <div class="site">
      <span class="site-rule"></span>
      <span class="site-url">www.fernhollowturf<span class="tld">.org</span></span>
    </div>
  </main>
</body>
</html>
```